Redesign lumenvale.com home page

We want to improve our website design overall, show us what you can do with our home page and we will move forward with the best designer to redo the other pages on our site.

Particularly interested in redesigning the header/footer.

Target Market(s)

scientists and engineers

Number of Pages Required

1 page

Font styles to use
Sans Serif

Requirements
Nice to have
• More grey and red and less black than we have now for the header

```html
<!DOCTYPE html>
<html lang="en">
<head>
<meta charset="utf-8">
<title>Lumenvale Optics Corporation</title>
<link rel="stylesheet" href="https://fonts.googleapis.com/css2?family=Open+Sans:ital,wght@0,400;0,600;0,700;1,400&family=Roboto+Condensed:wght@400;700&display=swap">
<style>
:root{
  --red:#c8222a;
  --ink:#2b2b2b;
  --text:#555;
  --muted:#777;
  --light:#f4f4f4;
  --line:#e2e2e2;
  --footer:#3a3a3a;
  --footer-deep:#2c2c2c;
  --white:#fff;
}
*{margin:0;padding:0;box-sizing:border-box}
html,body{width:1200px;height:2980px;overflow:hidden}
body{position:relative;background:var(--white);font-family:"Open Sans",Arial,sans-serif;color:var(--text)}
a{text-decoration:none}
.abs{position:absolute}
.head-font{font-family:"Roboto Condensed","Arial Narrow",sans-serif}

/* header */
.site-header{position:absolute;left:0;top:0;width:1200px;height:104px;background:var(--white)}
.brand{left:100px;top:36px;display:flex;align-items:center;gap:10px}
.brand-mark{width:30px;height:30px;background:var(--red)}
.brand-name{font-weight:700;font-size:16px;color:var(--ink);letter-spacing:.5px}
.nav{right:98px;top:38px;display:flex;gap:50px;font-size:12.5px;color:#444;text-transform:uppercase}
.nav a{color:inherit;position:relative}
.nav a.active{color:var(--red)}
.nav a.active::after{content:"";position:absolute;left:50%;margin-left:-40px;top:34px;width:80px;height:2px;background:var(--red)}

/* hero */
.hero{left:0;top:104px;width:1200px;height:476px;background:radial-gradient(ellipse at 70% 40%,#3b5a8c 0%,#1a2c52 40%,#0b1328 75%),#0b1328}
.hero-earth{left:0;top:330px;width:1200px;height:146px;background:linear-gradient(180deg,rgba(90,140,200,0) 0%,rgba(120,170,220,.55) 60%,rgba(200,220,240,.7) 100%)}
.hero-craft{left:560px;top:40px;width:520px;height:300px;background:radial-gradient(ellipse at center,rgba(200,170,110,.55) 0%,rgba(80,110,170,.35) 45%,rgba(0,0,0,0) 70%)}
.hero-title{left:100px;top:120px;font-size:41px;font-weight:700;color:var(--white);text-transform:uppercase}
.hero-sub{left:100px;top:186px;width:620px;font-size:13.5px;font-style:italic;color:#e8ecf4;line-height:22px}
.btn{display:inline-block;background:var(--red);color:var(--white);font-size:12.5px;font-weight:600;text-transform:uppercase;text-align:center;border-radius:3px}
.hero-btn{left:100px;top:258px;width:128px;height:48px;line-height:48px}
.dots{left:100px;top:340px;display:flex;gap:8px}
.dots span{width:9px;height:9px;border-radius:50%;background:var(--white)}
.dots span.on{background:var(--red)}

/* who we are */
.section-title{font-size:30px;font-weight:400;color:var(--ink);text-transform:uppercase}
.who-title{left:100px;top:650px}
.who-text{left:100px;top:700px;width:550px;font-size:12.6px;line-height:25px;color:var(--text)}
.who-text p+p{margin-top:6px}
.who-btn{left:100px;top:976px;width:127px;height:48px;line-height:48px}
.who-photo{left:670px;top:660px;width:432px;height:366px;background:linear-gradient(170deg,#05070d 0%,#0d1322 55%,#274b7e 85%,#6e8fb6 100%)}

/* services */
.services{left:0;top:1100px;width:1200px;height:486px;background:var(--light)}
.center-title{width:1200px;left:0;text-align:center}
.rule{left:570px;width:60px;height:3px;background:var(--red)}
.service{width:320px;display:flex;gap:18px}
.ring{flex:none;width:80px;height:80px;border-radius:50%;border:2px solid var(--red);display:flex;align-items:center;justify-content:center;background:var(--white)}
.ring.filled{background:var(--red)}
.service h3{font-size:12.5px;font-weight:700;color:var(--ink);text-transform:uppercase;margin:4px 0 6px;line-height:18px;white-space:nowrap}
.service p{font-size:12px;line-height:22px;color:var(--text)}
.service .more{color:var(--red)}

/* news */
.news-card{width:310px}
.news-photo{height:180px;border:4px solid #e9e9e9}
.news-card h3{font-size:14px;font-weight:600;color:var(--ink);text-transform:uppercase;line-height:24px;margin-top:26px}
.news-date{font-size:10.5px;color:var(--red);margin-top:10px;display:flex;align-items:center;gap:6px}
.news-card p{font-size:11.5px;line-height:20px;margin-top:6px}
.btn-line{display:inline-block;margin-top:14px;border:1px solid var(--red);color:var(--red);font-size:11px;padding:5px 8px;text-transform:uppercase}

/* testimonial */
.quote-band{left:0;top:2195px;width:1200px;height:220px;background:var(--light)}
.avatar{left:146px;top:2220px;width:122px;height:122px;border-radius:50%;background:radial-gradient(circle at 50% 45%,#d9b79a 0%,#b08a6c 50%,#e6e6e6 72%);border:4px solid #ececec}
.quote{left:300px;top:2244px;width:760px;font-size:12.6px;font-style:italic;line-height:24px;color:#666}
.quote-by{left:300px;top:2330px;font-size:16px;font-style:italic}
.quote-by b{color:var(--red);font-weight:600}
.quote-by span{color:var(--ink)}
.arrows{left:1000px;top:2330px;display:flex;gap:24px}

/* badges */
.badge-box{top:2484px;width:200px;height:96px;border:1px solid var(--line);display:flex;align-items:center;justify-content:center}

/* footer */
.footer{left:0;top:2655px;width:1200px;height:275px;background:var(--footer)}
.footer-col{position:absolute;top:48px;color:#e6e6e6;font-size:12.5px}
.footer-col h4{font-size:15px;font-weight:600;color:var(--white);text-transform:uppercase;margin-bottom:18px;line-height:20px}
.contact-row{display:flex;gap:18px;line-height:26px;margin-bottom:8px;align-items:flex-start}
.contact-row svg{margin-top:5px;flex:none}
.links{list-style:none}
.links li{line-height:32px;display:flex;gap:20px;align-items:center}
.social{list-style:none}
.social li{display:flex;gap:14px;align-items:center;height:37px}
.soc-icon{width:24px;height:24px;border-radius:50%;border:1.5px solid #ddd}
.field{width:288px;height:42px;border:1px solid #cfcfcf;color:var(--white);font-size:12px;padding:12px 14px;margin-bottom:8px}
.sub-btn{width:102px;height:40px;line-height:40px;margin-top:8px;border-radius:0}
.bottom-bar{left:0;top:2930px;width:1200px;height:50px;background:var(--footer-deep);color:#ddd;font-size:12.5px;text-align:center;line-height:50px}
</style>
</head>
<body>

<header class="site-header">
  <div class="abs brand"><span class="brand-mark"></span><span class="brand-name">LUMENVALE OPTICS CORPORATION</span></div>
  <nav class="abs nav">
    <a class="active" href="#">Products &amp; Services</a>
    <a href="#">News</a>
    <a href="#">Applications</a>
    <a href="#">Company</a>
    <a href="#">Contact Us</a>
  </nav>
</header>

<section class="abs hero">
  <div class="abs hero-earth"></div>
  <div class="abs hero-craft" role="img" aria-label="Satellite with solar panels orbiting above Earth"></div>
  <h1 class="abs hero-title">Welcome to Lumenvale Optics</h1>
  <p class="abs hero-sub">Lumenvale Optics Corporation offers a single engineering and manufacturing source for characterization, control, and exploitation of the optical properties of surfaces.</p>
  <a class="abs btn hero-btn" href="#">Get Started</a>
  <div class="abs dots"><span class="on"></span><span></span><span></span><span></span><span></span></div>
</section>

<h2 class="abs section-title head-font who-title">Who We Are</h2>
<div class="abs who-text">
  <p>Founded in 1978, Lumenvale Optics Corporation (LOC) is an employee-owned small business firm specializing in the characterization and exploitation of the optical properties of surfaces. For over ement services under Government and commercial contracts and developed an extensive data base of optical measurements for a wide variety of materials.</p>
  <p>Lumenvale Optics Corporation offers a single engineering and manufacturing source for characterization, control, and exploitation of the optical properties of surfaces. Our unique understanding of customers' needs allows us to offer engineering services, proprietary analytical software, reflectometers, hyperspectral and multispectral imagers, and surface coating products that are cost effective, innovative, and provide unsurpassed performance.</p>
</div>
<a class="abs btn who-btn" href="#">Read More</a>
<div class="abs who-photo" role="img" aria-label="Space station orbiting above Earth against a starfield"></div>

<section class="abs services"></section>
<h2 class="abs section-title head-font center-title" style="top:1180px">Our Services</h2>
<div class="abs rule" style="top:1230px"></div>

<div class="abs service" style="left:98px;top:1280px">
  <div class="ring filled"><svg width="36" height="36" viewBox="0 0 36 36"><circle cx="18" cy="18" r="11" fill="none" stroke="#fff" stroke-width="6" stroke-dasharray="4 3.2"/><circle cx="18" cy="18" r="8" fill="#fff"/><circle cx="18" cy="18" r="4" fill="#c8222a"/></svg></div>
  <div><h3>R&amp;D Engineering Services</h3><p>Expert support for projects in optical phenomenology and measurements, and instruments <span class="more">&gt;&gt;</span></p></div>
</div>
<div class="abs service" style="left:432px;top:1280px">
  <div class="ring"><svg width="34" height="38" viewBox="0 0 34 38" fill="none" stroke="#c8222a" stroke-width="2.2"><ellipse cx="17" cy="8" rx="10" ry="4"/><path d="M9 12 L6 36 M25 12 L28 36 M8 24 H26 M10 18 L24 30 M24 18 L10 30"/></svg></div>
  <div><h3>Vacuum Deposition Coatings</h3><p>Utilizing chambers from one meter diameter to 3 meter diameter, we develop coatings <span class="more">&gt;&gt;</span></p></div>
</div>
<div class="abs service" style="left:766px;top:1280px">
  <div class="ring"><svg width="34" height="34" viewBox="0 0 34 34" fill="#c8222a"><path d="M4 30 H30 V27 H4 Z"/><path d="M6 25 L18 10 L22 14 L10 25 Z"/><path d="M20 8 L27 4 L30 7 L24 12 Z"/></svg></div>
  <div><h3>Optical Properties Measurements</h3><p>World-class measurement facility and industry leader in supplying high quality spectral directional <span class="more">&gt;&gt;</span></p></div>
</div>
<div class="abs service" style="left:98px;top:1415px">
  <div class="ring"><svg width="36" height="30" viewBox="0 0 36 30"><rect x="2" y="2" width="32" height="26" fill="none" stroke="#c8222a" stroke-width="3"/><path d="M6 24 L14 14 L20 20 L24 16 L30 24 Z" fill="#c8222a"/><circle cx="25" cy="9" r="3" fill="#c8222a"/></svg></div>
  <div><h3>Hyperspectral and Multispe<br>ctral Imaging</h3><p>Dual-band and four-band high spatial resolution and high-speed <span class="more">&gt;&gt;</span></p></div>
</div>
<div class="abs service" style="left:432px;top:1415px">
  <div class="ring"><svg width="34" height="34" viewBox="0 0 34 34" fill="#c8222a"><path d="M22 4 L30 12 L27 15 L19 7 Z"/><path d="M18 10 L24 16 L10 30 L4 30 L4 24 Z"/></svg></div>
  <div><h3>Pigmented Coatings</h3><p>Using our analytical expertise, we formulate and produce spectrally tailored paints signature <span class="more">&gt;&gt;</span></p></div>
</div>
<div class="abs service" style="left:766px;top:1415px">
  <div class="ring"><svg width="30" height="38" viewBox="0 0 30 38"><rect x="3" y="2" width="24" height="26" rx="12" fill="#c8222a"/><circle cx="15" cy="14" r="6" fill="#fff"/><rect x="11" y="28" width="8" height="8" fill="#c8222a"/></svg></div>
  <div><h3>Reflectometer Instrumentation</h3><p>Laboratory, field-portable, and hand-held systems fully characterize surface scattering from <span class="more">0.4 µm to 12 µm</span></p></div>
</div>

<h2 class="abs section-title head-font center-title" style="top:1650px">Recent News</h2>
<div class="abs rule" style="top:1700px"></div>

<article class="abs news-card" style="left:98px;top:1754px">
  <div class="news-photo" role="img" aria-label="Armored military vehicle on display outdoors" style="background:linear-gradient(180deg,#d8dde2 0%,#b59c6e 45%,#7c6a4c 100%)"></div>
  <h3>Multispectral Technology Advan cement Industry Day</h3>
  <div class="news-date"><svg width="9" height="9" viewBox="0 0 9 9"><rect width="9" height="9" fill="#c8222a"/></svg>On October 25, 2016</div>
  <p>The Regional Defense Program Office (RDPO) program demonstrated Lumenvale Optics..</p>
  <a class="btn-line" href="#">Read More ⊕</a>
</article>
<article class="abs news-card" style="left:446px;top:1754px">
  <div class="news-photo" role="img" aria-label="Coated metallic ring component on a lab bench" style="background:linear-gradient(180deg,#8a7f72 0%,#d6d2cc 45%,#b7a994 100%)"></div>
  <h3>Thermal Control Coating Applied to Horizon Mars Lander</h3>
  <div class="news-date"><svg width="9" height="9" viewBox="0 0 9 9"><rect width="9" height="9" fill="#c8222a"/></svg>On October 19, 2016</div>
  <p>Lumenvale Optics Corporation (LOC) has been contracted to supply a thermal the Agency's Lander..</p>
  <a class="btn-line" href="#">Read More ⊕</a>
</article>
<article class="abs news-card" style="left:792px;top:1754px">
  <div class="news-photo" role="img" aria-label="Analysts working at computer screens in a dim office" style="background:linear-gradient(180deg,#3a2f28 0%,#5a4a3c 50%,#2e3b44 100%)"></div>
  <h3>Hyperspectral Imaging Possible Harriet Vance Wreckage</h3>
  <div class="news-date"><svg width="9" height="9" viewBox="0 0 9 9"><rect width="9" height="9" fill="#c8222a"/></svg>On August 28, 2014</div>
  <p>An aircraft recovery group will collect hyperspectral data using the LV710-VP for evidence as piece..</p>
  <a class="btn-line" href="#">Read More ⊕</a>
</article>

<section class="abs quote-band"></section>
<div class="abs avatar" role="img" aria-label="Portrait of a client"></div>
<p class="abs quote">“ All the Lorem Ipsum generators on the Internet tend to repeat predefined chunks as necessary, making this the first true generator on the Internet. It uses a dictionary of over 200 Latin words, combined with a handful of model sentence structures, to generate Lorem Ipsum which looks reasonable. The generated Lorem Ipsum is therefore always free from repetition ”</p>
<p class="abs quote-by"><b>Daniel Reyes</b><span>, Lorem ipsum</span></p>
<div class="abs arrows">
  <svg width="14" height="20" viewBox="0 0 14 20"><path d="M11 2 L3 10 L11 18" fill="none" stroke="#c8222a" stroke-width="2.5"/></svg>
  <svg width="14" height="20" viewBox="0 0 14 20"><path d="M3 2 L11 10 L3 18" fill="none" stroke="#c8222a" stroke-width="2.5"/></svg>
</div>

<div class="abs badge-box" style="left:166px"><svg width="110" height="40"><rect width="110" height="40" rx="4" fill="#1f3a6b" opacity=".85"/></svg></div>
<div class="abs badge-box" style="left:390px"><svg width="60" height="60"><circle cx="30" cy="30" r="28" fill="#1f4f9a"/></svg></div>
<div class="abs badge-box" style="left:614px"><svg width="44" height="72"><rect width="44" height="72" fill="#333"/></svg></div>
<div class="abs badge-box" style="left:836px"><svg width="80" height="60"><rect width="80" height="60" rx="4" fill="#3b6ea8"/></svg></div>

<footer class="abs footer">
  <div class="footer-col" style="left:100px">
    <h4>Contact Us</h4>
    <div class="contact-row"><svg width="16" height="16" viewBox="0 0 16 16" fill="#fff"><path d="M8 1 L1 8 H3 V15 H7 V10 H9 V15 H13 V8 H15 Z"/></svg><span>4820 Meridian Ridge Rd.<br>San Diego, CA 92130</span></div>
    <div class="contact-row"><svg width="16" height="20" viewBox="0 0 16 20"><rect x="3" y="1" width="10" height="18" rx="2" fill="none" stroke="#fff" stroke-width="2"/></svg><span>Call Us : 858-555-0142</span></div>
    <div class="contact-row"><svg width="16" height="16" viewBox="0 0 16 16"><rect x="1" y="3" width="14" height="10" fill="none" stroke="#fff" stroke-width="1.6"/><path d="M1 3 L8 9 L15 3" fill="none" stroke="#fff" stroke-width="1.6"/></svg><span>contact@lumenvale.com</span></div>
  </div>
  <div class="footer-col" style="left:372px">
    <h4>Quick Links</h4>
    <ul class="links">
      <li><svg width="8" height="10" viewBox="0 0 8 10"><path d="M1 1 L6 5 L1 9" fill="none" stroke="#fff" stroke-width="2"/></svg><span>Home</span></li>
      <li><svg width="8" height="10" viewBox="0 0 8 10"><path d="M1 1 L6 5 L1 9" fill="none" stroke="#fff" stroke-width="2"/></svg><span>Products &amp; Services</span></li>
      <li><svg width="8" height="10" viewBox="0 0 8 10"><path d="M1 1 L6 5 L1 9" fill="none" stroke="#fff" stroke-width="2"/></svg><span>News</span></li>
      <li><svg width="8" height="10" viewBox="0 0 8 10"><path d="M1 1 L6 5 L1 9" fill="none" stroke="#fff" stroke-width="2"/></svg><span>Applications</span></li>
      <li><svg width="8" height="10" viewBox="0 0 8 10"><path d="M1 1 L6 5 L1 9" fill="none" stroke="#fff" stroke-width="2"/></svg><span>Company</span></li>
    </ul>
  </div>
  <div class="footer-col" style="left:604px">
    <h4>Social Media</h4>
    <ul class="social">
      <li><span class="soc-icon"></span>Friendlink</li>
      <li><span class="soc-icon"></span>Chirper</li>
      <li><span class="soc-icon"></span>Worknet</li>
      <li><span class="soc-icon"></span>Clipstream</li>
    </ul>
  </div>
  <div class="footer-col" style="left:816px">
    <h4>Contact Form</h4>
    <div class="field">Enter Name</div>
    <div class="field">Enter Mail</div>
    <a class="btn sub-btn" href="#">Subscribe</a>
  </div>
</footer>
<div class="abs bottom-bar">© &nbsp;Lumenvale Optics Corporation 2017 . All Rights Reserved</div>

</body>
</html>
```